TVQ-Business Card Design

I need a modern, professional business card design that includes my logo as the main feature, maybe the entire background with the contact info overlaying or even contact info on the back and the logo full frontal

Neat and organized placement of contact information

Would like to see options in black and white

Target Market(s)

real estate Developers, Construction managers, business and home owners

Industry/Entity Type

Construction

Contact Information for Business Card

TVQ Construction
Dennis Fairweather
General Contractor

Office: 1-888-902-7351 Ext #1
Cell: 412-730-2168
Fax: 1-888-902-7351

Font styles to use
Serif

Requirements
Must have
• title
• office #
• cell #
• Email
• website
Nice to have
• fax

```html
<!DOCTYPE html>
<html lang="en">
<head>
<meta charset="utf-8">
<title>TVQ Construction – Business Card</title>
<link href="https://fonts.googleapis.com/css2?family=Roboto:wght@400;700;900&family=Roboto+Mono:wght@400;700&display=swap" rel="stylesheet">
<style>
  :root {
    --backdrop: #285c3e;
    --card: #ffffff;
    --brand-green: #009444;
    --brand-deep: #00632f;
    --ink: #1c1c1c;
    --muted: #444444;
  }
  * { box-sizing: border-box; margin: 0; padding: 0; }
  html, body {
    width: 1200px;
    height: 900px;
    overflow: hidden;
    background: var(--backdrop);
    font-family: "Roboto", Arial, sans-serif;
  }
  .card {
    position: absolute;
    left: 280px;
    width: 640px;
    height: 366px;
    background: var(--card);
    box-shadow: 0 6px 18px rgba(0,0,0,0.25);
    overflow: hidden;
  }
  .card--front { top: 60px; }
  .card--back { top: 474px; }

  .brand-name {
    display: flex;
    align-items: center;
    gap: 12px;
    color: var(--brand-green);
    font-weight: 900;
    letter-spacing: 0.5px;
    white-space: nowrap;
  }
  .brand-name__mark {
    background: var(--brand-green);
    flex: none;
  }
  .card--front .brand-name {
    position: absolute;
    left: 0; right: 0; top: 0; bottom: 0;
    justify-content: center;
    font-size: 44px;
  }
  .card--front .brand-name__mark { width: 30px; height: 30px; }

  .card--back .brand-name {
    position: absolute;
    right: 100px;
    top: 42px;
    font-size: 24px;
    z-index: 1;
  }
  .card--back .brand-name__mark { width: 16px; height: 16px; }

  .swoosh {
    position: absolute;
    right: 0; top: 0;
    width: 640px; height: 366px;
  }

  .contact {
    position: absolute;
    left: 44px;
    bottom: 44px;
  }
  .contact__name {
    color: var(--brand-green);
    font-weight: 900;
    font-size: 24px;
    letter-spacing: 0.3px;
  }
  .contact__title {
    font-size: 12px;
    font-weight: 700;
    color: var(--muted);
    letter-spacing: 0.6px;
    margin-bottom: 18px;
  }
  .contact__lines {
    font-family: "Roboto Mono", monospace;
    font-size: 13px;
    color: var(--ink);
    line-height: 1.45;
  }
  .contact__row { display: flex; }
  .contact__label { width: 62px; }
  .contact__web {
    margin-top: 14px;
    font-family: "Roboto Mono", monospace;
    font-size: 13px;
    font-weight: 700;
    color: var(--brand-green);
    letter-spacing: 0.4px;
  }
</style>
</head>
<body>
  <section class="card card--front" aria-label="Card front">
    <div class="brand-name">
      <span class="brand-name__mark"></span>
      <span>TVQ Construction</span>
    </div>
  </section>

  <section class="card card--back" aria-label="Card back">
    <svg class="swoosh" viewBox="0 0 640 366" aria-hidden="true">
      <path d="M575 0 C560 150 505 285 440 366 L640 366 L640 0 Z" fill="var(--brand-green)"/>
      <path d="M640 70 C610 190 570 290 515 366 L640 366 Z" fill="var(--brand-deep)"/>
    </svg>

    <div class="brand-name">
      <span class="brand-name__mark"></span>
      <span>TVQ Construction</span>
    </div>

    <div class="contact">
      <div class="contact__name">DENNIS FAIRWEATHER</div>
      <div class="contact__title">General Contractor</div>
      <div class="contact__lines">
        <div class="contact__row"><span class="contact__label">Office</span><span>1-888-902-7351 Ext #1</span></div>
        <div class="contact__row"><span class="contact__label">Cell</span><span>412-730-2168</span></div>
        <div class="contact__row"><span class="contact__label">Fax</span><span>1-888-902-7351</span></div>
        <div class="contact__row"><span>dennis@TVQConstruction.com</span></div>
      </div>
      <div class="contact__web">www.TVQConstruction.com</div>
    </div>
  </section>
</body>
</html>
```